High-end residential home builder needs a business card design

We need a new business card design for a small residential construction company based in Boise, Idaho. We specialize in building custom high-end homes and remodels, with a focus on great design and craftsmanship.

We would like to use our current logo, but open to new color suggestions.
Just looking for a clean, sharp, modern design that looks high-end.

Target Market(s)

Upscale clientele

Industry/Entity Type

Contractor

Contact Information for Business Card

Company: Stonefield Custom Builders
Name: Marcus Tilley
Phone number: 208 367 4120
Email: MarcusTilleySCB@mailbox-example.com
Website: Stonefieldcustombuilders-example.com

Font styles to use
Serif
Sans Serif

Requirements
Must have
• Company Logo
Company name
My name
My phone number
My email
Company website
Nice to have
• I have attached a few photos of cards that I really like.

```html
<!DOCTYPE html>
<html lang="en">
<head>
<meta charset="utf-8">
<title>Stonefield Custom Builders – Business Card</title>
<link href="https://fonts.googleapis.com/css2?family=Open+Sans:wght@400;600;700&display=swap" rel="stylesheet">
<style>
  :root {
    --backdrop: #cfcfcf;
    --card: #242424;
    --ink: #ffffff;
    --accent: #d98a1f;
    --rule: #8a8a8a;
  }
  * { box-sizing: border-box; margin: 0; padding: 0; }
  html, body {
    width: 1200px; height: 900px; overflow: hidden;
    background: var(--backdrop);
    font-family: "Open Sans", Arial, sans-serif;
  }
  .card {
    position: absolute;
    width: 560px; height: 320px;
    background: var(--card);
    box-shadow: 0 6px 18px rgba(0,0,0,0.25);
    overflow: hidden;
  }
  .card--back { left: 80px; top: 110px; }
  .card--front { left: 560px; top: 470px; }

  .brand {
    display: flex; align-items: center; gap: 18px;
  }
  .brand__mark {
    width: 46px; height: 46px;
    border: 3px solid var(--ink);
    flex: none;
  }
  .brand__name {
    color: var(--ink);
    font-weight: 600;
    text-transform: uppercase;
    letter-spacing: 0.22em;
    line-height: 1.45;
    font-size: 15px;
  }
  .card--back .brand {
    position: absolute; left: 50%; top: 50%;
    transform: translate(-50%, -50%);
  }

  .card--front .brand {
    position: absolute; left: 60px; top: 58px;
  }
  .card--front .brand__name { font-size: 17px; }

  .person {
    position: absolute; left: 30px; top: 200px; width: 190px;
    text-align: right;
  }
  .person__name { color: var(--ink); font-weight: 700; font-size: 20px; }
  .person__role { color: var(--accent); font-weight: 400; font-size: 15px; margin-top: 2px; }

  .divider {
    position: absolute; left: 236px; top: 190px;
    width: 1px; height: 76px; background: var(--rule);
  }

  .contact {
    position: absolute; left: 252px; top: 192px; width: 268px;
    list-style: none;
    color: var(--ink); font-size: 12px;
  }
  .contact li { display: flex; align-items: center; gap: 8px; height: 24px; white-space: nowrap; }
  .contact svg { width: 13px; height: 13px; flex: none; fill: none; stroke: var(--accent); stroke-width: 2; }
</style>
</head>
<body>

<section class="card card--back" aria-label="Card back">
  <div class="brand">
    <span class="brand__mark"></span>
    <span class="brand__name">Stonefield<br>Custom Builders</span>
  </div>
</section>

<section class="card card--front" aria-label="Card front">
  <div class="brand">
    <span class="brand__mark"></span>
    <span class="brand__name">Stonefield<br>Custom Builders</span>
  </div>

  <div class="person">
    <p class="person__name">Marcus Tilley</p>
    <p class="person__role">Founder</p>
  </div>

  <span class="divider"></span>

  <ul class="contact">
    <li>
      <svg viewBox="0 0 16 16"><path d="M4 1.5 6.5 4 5 6.5c1 2 2.5 3.5 4.5 4.5L12 9.5l2.5 2.5-2 2C7 13.5 2.5 9 2 3.5z"/></svg>
      208 367 4120
    </li>
    <li>
      <svg viewBox="0 0 16 16"><rect x="1.5" y="3.5" width="13" height="9"/><path d="M1.5 3.5 8 9l6.5-5.5"/></svg>
      MarcusTilleySCB@mailbox-example.com
    </li>
    <li>
      <svg viewBox="0 0 16 16"><circle cx="8" cy="8" r="6.5"/><path d="M1.5 8h13M8 1.5c-3 3.5-3 9.5 0 13M8 1.5c3 3.5 3 9.5 0 13"/></svg>
      Stonefieldcustombuilders-example.com
    </li>
  </ul>
</section>

</body>
</html>
```